website re-design - the brickfern studio

The Brickfern Studio is an existing website that we built using a new zealand based online CMS tool which is quite flexible and accomodates custom designs. You can check it here: http://www.pagequilt.co.nz/.

We have a logo already and the content on the website is OK.
The website can be found at www.thebrickfernstudio.com.au

mainly the homepage, but if the design is easily adapted to the other pages then, we will commission the winner to update these pages also.
Updates

Hi there,  I am uploading an image to be used as the main image on the homepage design,  so all submissions have the same image.

Target Market(s)

property developers, architects, builders, home buyers

Industry/Entity Type

Shop

Requirements
Must have
• Must utilise the existing CMS or at least be compatible to upload
Nice to have
• a promotional banner that can be turned off and on and changed as required as we offer different promotions over time.

```html
<!DOCTYPE html>
<html lang="en">
<head>
<meta charset="utf-8">
<title>The Brickfern Studio – Architectural Scale Models</title>
<link href="https://fonts.googleapis.com/css2?family=Arimo:wght@400;700&family=Lora:ital,wght@1,400;1,700&display=swap" rel="stylesheet">
<style>
:root{
  --orange:#ee7c1d;
  --orange-dark:#c8400f;
  --text:#333;
  --muted:#666;
  --rule:#ddd;
  --band:#ececec;
  --footer:#1c1c1c;
  --white:#fff;
}
*{box-sizing:border-box;margin:0;padding:0}
html,body{width:943px;height:1200px;overflow:hidden}
body{position:relative;background:var(--white);font-family:"Arimo",Arial,sans-serif;color:var(--text);font-size:12px}
.abs{position:absolute}
.top-rule{left:0;top:0;width:943px;height:6px;background:var(--orange)}
.brand{left:0;top:30px;width:943px;display:flex;justify-content:center;align-items:center;gap:18px}
.brand-mark{width:70px;height:70px;border:3px solid var(--orange)}
.brand-name{font-size:32px;color:#555;font-weight:400;letter-spacing:.5px;line-height:1}
.brand-tag{font-size:15px;color:var(--orange);letter-spacing:1px;margin-top:6px}
.nav{left:0;top:145px;width:943px;height:41px;background:linear-gradient(#fff,#f1f1f1);border-top:1px solid var(--rule);border-bottom:3px solid var(--orange);display:flex;padding-left:44px}
.nav a{flex:none;white-space:nowrap;text-align:center;font-size:13px;color:#333;text-decoration:none;line-height:38px;border-right:1px solid var(--rule)}
.nav a:last-child{border-right:0}
.nav a.current{background:var(--orange);color:var(--white)}
.hero{left:44px;top:204px;width:853px;height:313px;border:4px solid #fff;box-shadow:0 0 4px #aaa;background:linear-gradient(180deg,#2e4d78 0%,#3f5f82 30%,#4f6a66 60%,#27492f 100%)}
.hero-panel{left:628px;top:239px;width:232px;height:246px;background:rgba(30,30,30,.72);border:1px solid #888;padding:14px 16px;color:#fff}
.hero-panel h2{font-family:"Lora",Georgia,serif;font-style:italic;font-weight:400;color:var(--orange);font-size:23px;line-height:1.2;margin-bottom:12px}
.hero-panel p{font-size:12.5px;line-height:1.75}
.strip{left:0;top:538px;width:943px;height:82px;background:linear-gradient(#f4f4f4,#e2e2e2)}
.thumb{top:546px;width:120px;height:60px;background:linear-gradient(#c9d4dc 0%,#a8786a 45%,#f1f1f1 70%,#6f8a58 100%)}
.arrow{top:562px}
.col-rule{left:630px;top:640px;width:1px;height:470px;background:var(--rule)}
.quote{left:44px;top:657px;width:567px;text-align:center;font-family:"Lora",Georgia,serif;font-style:italic;font-size:17px;color:#444}
.intro{left:44px;top:697px;width:570px;font-size:11px;line-height:1.85;color:#555}
.intro em{font-style:normal;color:var(--orange)}
.qlist{left:50px;top:800px;width:568px;list-style:none}
.qlist li{position:relative;padding-left:28px;font-weight:700;font-size:11px;letter-spacing:-.1px;line-height:1.45;margin-bottom:10px}
.qlist li::before{content:"";position:absolute;left:2px;top:3px;width:11px;height:11px;border-radius:50%;background:#f6d9c0;box-shadow:inset 0 0 0 3px #fbeee2}
.qlist li::after{content:"";position:absolute;left:6px;top:7px;width:4px;height:4px;border-radius:50%;background:var(--orange)}
.call{left:44px;top:998px;width:202px;height:73px;border:1px solid #ccc;border-radius:4px;background:linear-gradient(#fff,#e8e8e8)}
.call-label{right:14px;top:12px;font-size:13px;color:#333}
.call-num{right:10px;top:36px;font-size:16px;color:#444;white-space:nowrap}
.phone-icon{left:6px;top:14px}
.testimonial{left:267px;top:998px;width:340px;height:76px;border:1px solid var(--rule);box-shadow:0 1px 3px #ccc;padding:8px 14px 0 50px;font-size:11px;line-height:1.6;color:#888}
.testimonial .mark{position:absolute;left:12px;top:0;font-family:"Lora",Georgia,serif;font-size:46px;color:#ddd}
.author{left:492px;top:1076px;font-family:"Lora",Georgia,serif;font-style:italic;font-size:15px;color:var(--orange)}
.side-title{left:649px;top:645px;font-size:15.5px;color:#333;letter-spacing:.3px}
.steps{left:651px;top:676px;width:275px;list-style:none}
.steps li{display:flex;gap:14px;font-weight:700;font-size:11.5px;line-height:1.6;margin-bottom:6px}
.steps span{flex:none;width:20px;height:20px;border-radius:50%;background:var(--orange);color:#fff;font-size:11px;text-align:center;line-height:20px}
.btn{left:653px;width:228px;height:42px;text-align:center;line-height:42px;font-weight:700;font-size:12.5px}
.btn-quote{top:754px;background:linear-gradient(90deg,var(--orange),var(--orange-dark));color:#fff}
.btn-order{top:813px;background:linear-gradient(#fff,#eee);border:1px solid var(--rule);color:#333;box-shadow:0 2px 3px #ccc}
.side-copy{left:649px;top:878px;width:258px;font-size:11px;letter-spacing:-.1px;line-height:19px;color:#555}
.side-copy p{margin-bottom:14px}
.shares{left:649px;top:1078px;display:flex;gap:16px}
.share{display:flex;gap:3px;font-size:10px}
.share b{background:#e7eef6;border:1px solid #bcc;padding:2px 6px;font-weight:400}
.share i{font-style:normal;border:1px solid #ccc;padding:2px 6px;color:#555}
.footer{left:0;top:1127px;width:943px;height:73px;background:var(--footer)}
.foot-links{left:44px;top:1143px;font-size:10.5px;color:#ddd}
.foot-links a{color:#ddd;text-decoration:none;margin-right:8px}
.foot-links span{margin-right:8px}
.foot-copy{left:44px;top:1170px;font-size:10px;color:#888}
.foot-mark{left:848px;top:1128px;width:52px;height:32px;border:2px solid var(--orange)}
.foot-social{top:1170px;width:16px;height:16px;background:#5a86b8}
</style>
</head>
<body>
<div class="abs top-rule"></div>

<header class="abs brand">
  <div class="brand-mark"></div>
  <div>
    <div class="brand-name">THE BRICKFERN STUDIO</div>
    <div class="brand-tag">ARCHITECTURAL SCALE MODELS</div>
  </div>
</header>

<nav class="abs nav">
  <a class="current" href="#" style="width:76px">HOME</a>
  <a href="#" style="width:85px">GALLERY</a>
  <a href="#" style="width:129px">ORDER ONLINE</a>
  <a href="#" style="width:116px">GET A QUOTE</a>
  <a href="#" style="width:118px">CONTACT US</a>
  <a href="#" style="width:144px">3D VISUALISATION</a>
  <a href="#" style="width:94px">ABOUT US</a>
  <a href="#" style="width:93px">SITE MAP</a>
</nav>

<div class="abs hero" role="img" aria-label="Evening aerial rendering of a modern apartment development with a pool and gardens"></div>
<div class="abs hero-panel">
  <h2>Lorem ipsum dolor sit amet,</h2>
  <p>Lorem ipsum dolor sit amet, consectetuer adipiscing elit. Aenean commodo ligula eget dolor. Aenean massa. Cum sociis natoque penatibus et magnis dis parturient montes, nascetur ridiculus mus.</p>
</div>

<div class="abs strip"></div>
<svg class="abs arrow" style="left:57px" width="30" height="32" viewBox="0 0 30 32"><path d="M24 2 8 16l16 14" fill="none" stroke="var(--orange)" stroke-width="7"/></svg>
<div class="abs thumb" style="left:105px" role="img" aria-label="Model of a two-storey house"></div>
<div class="abs thumb" style="left:257px" role="img" aria-label="Model of a two-storey house"></div>
<div class="abs thumb" style="left:410px" role="img" aria-label="Model of a two-storey house"></div>
<div class="abs thumb" style="left:562px" role="img" aria-label="Model of a two-storey house"></div>
<div class="abs thumb" style="left:714px" role="img" aria-label="Model of a two-storey house"></div>
<svg class="abs arrow" style="left:856px" width="30" height="32" viewBox="0 0 30 32"><path d="M6 2l16 14L6 30" fill="none" stroke="#fff" stroke-width="6"/><path d="M6 2l16 14L6 30" fill="none" stroke="#ccc" stroke-width="2"/></svg>

<div class="abs col-rule"></div>

<p class="abs quote">" a picture's worth a thousand words... a model says it all..."</p>
<div class="abs intro">
  <p>Getting an architectural model produced can be expensive and time consuming, but it can also add a lot of value to a project.&nbsp; A scale model lets everyone involved, get a very clear understanding of your building.</p>
  <p style="margin-top:22px">If you answered <em>yes</em> to any of the following questions, then you should be using the brickfern studio.</p>
</div>
<ul class="abs qlist">
  <li>Are you undertaking a new apartment development or land development and need a model for council approval or marketing purposes?</li>
  <li>Are you getting a new house designed and built and need a clear understanding of how it will look?</li>
  <li>Are you an architect or building designer looking for a more affordable way to add to your service?</li>
  <li>Are you wanting to clarify in your own mind how your new building sits on its site?</li>
  <li>Are you looking to for a way to market your buildings in an effective and affordable format that everyone can relate to?</li>
</ul>

<div class="abs call">
  <svg class="abs phone-icon" width="60" height="44" viewBox="0 0 72 50"><path d="M6 14c0-8 60-8 60 0v6H52v-4H20v4H6z" fill="#222"/><path d="M14 24h44l8 22H6z" fill="#2a2a2a"/><circle cx="36" cy="34" r="8" fill="#555"/><circle cx="36" cy="34" r="3" fill="#222"/></svg>
  <span class="abs call-label">CALL US</span>
  <span class="abs call-num">(08) 5550 0142</span>
</div>
<blockquote class="abs testimonial"><span class="mark">“</span>Lorem ipsum dolor sit amet, consectetuer adipiscing elit. Aenean commodo ligula eget dolor. Aenean massa. Cum sociis natoque penatibus et magnis</blockquote>
<span class="abs author">Martin</span>

<h3 class="abs side-title" style="font-weight:400">IT'S THIS EASY</h3>
<ol class="abs steps">
  <li><span>1</span>Order online or fill in the quote form.</li>
  <li><span>2</span>We'll build your model and deliver it<br>right to your door.</li>
</ol>
<a class="abs btn btn-quote">Click here to get a Quote.</a>
<a class="abs btn btn-order">Click here to Order your Model Now.</a>
<div class="abs side-copy">
  <p>You can tailor your model to suit your project and budget needs.&nbsp; There are various add-ons such as a display case, internal walls, acrylic windows, people trees and cars and site contours as well as a scaled pricing structure based on the size of your building.</p>
  <p>We have made the system very easy to use, so all you need to do is click your way to your new scale model. Just follow the prompts and away you go.</p>
</div>
<div class="abs shares">
  <div class="share"><b>Share</b><i>652</i></div>
  <div class="share"><b>Share</b><i>21</i></div>
  <div class="share"><b>Share</b><i>0</i></div>
</div>

<footer class="abs footer"></footer>
<div class="abs foot-links"><a href="#">Home</a><span>|</span><a href="#">Gallery</a><span>|</span><a href="#">Order Online</a><span>|</span><a href="#">Get a Quote</a><span>|</span><a href="#">Contact Us</a><span>|</span><a href="#">3d Visualisation</a><span>|</span><a href="#">About US</a><span>|</span><a href="#">Site map</a></div>
<div class="abs foot-copy">© Copyright The Brickfern Studio | &nbsp;Terms &amp; Conditions &nbsp;| &nbsp;Phone: (08) 5550 0142 Australia</div>
<div class="abs foot-mark"></div>
<div class="abs foot-social" style="left:860px"></div>
<div class="abs foot-social" style="left:882px"></div>
</body>
</html>
```